This is my scope and requirements:
Labelling project:
This is related to the Label project I also opened up. (The Brisk Owl Organic & Natural Soaps needs a good business card (Contest) )
I have attached an initial draft at a logo I tried to come up with for a business card and labelling/marketing. I am hoping that you can take this logo and 'run with it' to finesse it, make it look unique and professional. If you need to change it, I am open to ideas.
I find that labelling/packaging is hard for me to make it look 'professional' so I am coming to the experts!
I am looking for label designs for 2 different bottles and 2 different bar soaps:
1) Organic Bar Soap (2 possibilities: 1) Kraft 'cigar' band around soap with twine, 2) Kraft soap box with Kraft sticker Labels
2) Natural Olive Oil Based Bar Soap (labelling can be same as Organic but with distinct info)
3) Organic Hand Washes (clear square bottles, 250ml with natural pump)
4) Natural Olive Oil Based Body Wash (taper bottle 200ml with metal silver disc top caps)
I am a start up at home company making Organic and Natural Bar soaps, hand soaps, body washes.
All of my ingredients are organic or natural and will include natural essential oils, exfoliants, natural powders/colours, etc.
Some of the names are: Quillomé (feisty, energetic soap), Dunes (more of a sandalwood earthy tones with a sandalwood powder exfoliant), Frost (maybe changing this name - fresh scented), Amber Thyme (lemongrass/ginger, exfoliants), etc....
If you need more information, please let me know!
Please find attached: Kraft Paper I am looking at to possibly wrap the Bar Soaps in (I like the different colour concept and am trying to decide between diff colours of Ned Parrow paper to wrap around or plain kraft paper.. whichever the new logo concept will look best with.
The bottles I will be using for the hand soap (250ml square) and the body wash (200ml tapered)
OLD POST:
Hello! I am a start up business that is specializing in making luxury organic bar soaps, natural olive oil bar soaps, organic hand wash, natural olive oil body wash/shower gel that will include essential oils, exfoliants, natural powders, etc. (also accessories: wood soap dishes, etc) .. I am looking for a great designer that can provide me with the business card and labelling designs! I appreciate feedback, ideas on how I can receive a great design to help sell my products!
I am attaching my initial logo design that I would like to keep - but am looking for someone to 'finesse' it or make it more professional/unique looking.
Again, this is hand in hand with the business card project I submitted.
Thanks!
Verla
Updates
I am sorry for the lack of direction or Scope of the project. I am new at this board.
Labelling project:
I have attached an initial draft at a logo I tried to come up with for a business card and labelling/marketing. I am hoping that you can take this logo and 'run with it' to finesse it, make it look unique and professional.
If you need more information, please let me know.
Hello; I just wanted to let everyone know that if you feel that this brand needs a different logo, I am open to ideas (if you don't think the one I started with is ok). I am coming to the experts here!
Just to confirm also - this is related to the business card project, therefore, there are 2 projects, 2 payments! :)
Cheers
Industry/Entity Type
Business
Look and feel
Each slider illustrates characteristics of the customer's brand and the style your logo design should communicate.

```html
<!DOCTYPE html>
<html lang="en">
<head>
<meta charset="utf-8">
<title>The Brisk Owl – Bar Soap Labels</title>
<link rel="stylesheet" href="https://fonts.googleapis.com/css2?family=Crimson+Text:ital,wght@0,400;0,700;1,400;1,700&family=Lato:wght@400;700&family=Oleo+Script:wght@700&display=swap">
<style>
  :root {
    --page: #ffffff;
    --kraft: #c8ab88;
    --kraft-light: #d2b795;
    --frame: #3b2616;
    --panel: #7c5434;
    --panel-edge: #5e3d22;
    --crest: #ab9b75;
    --crest-edge: #4a3320;
    --ribbon: #f1e7c6;
    --ribbon-shade: #d9cba2;
    --brand-ink: #35412a;
    --ink: #24160c;
    --soap-tone: #efe2bf;
    --berry: #b5452e;
    --leaf: #6f7d4a;
    --olive: #c9a92e;
  }
  * { margin: 0; padding: 0; box-sizing: border-box; }
  html, body { width: 1200px; height: 918px; overflow: hidden; background: var(--page); }
  .sheet { position: relative; width: 1200px; height: 918px; }

  .label {
    position: absolute; top: 50px; width: 556px; height: 809px;
    background: radial-gradient(ellipse at 40% 35%, var(--kraft-light), var(--kraft) 70%);
  }
  .label--organic { left: 36px; }
  .label--olive { left: 607px; }
  .label__art { position: absolute; left: 0; top: 0; width: 556px; height: 809px; }

  .brand__name {
    position: absolute; left: 24px; width: 514px; top: 160px; text-align: center;
    font-family: "Crimson Text", serif; font-weight: 700; font-size: 64px; line-height: 72px;
    color: var(--brand-ink);
  }
  .brand__line {
    position: absolute; left: 88px; width: 384px; top: 260px; text-align: center;
    font-family: "Lato", sans-serif; font-weight: 700; font-size: 21px; line-height: 24px;
    letter-spacing: 1px; text-transform: uppercase; color: var(--ink);
  }

  .product {
    position: absolute; text-align: center; font-family: "Crimson Text", serif;
    color: var(--ink); line-height: 1;
  }
  .product__kind { font-size: 23px; }
  .product__type { font-size: 32px; }
  .product__natural { font-style: italic; font-size: 22px; }

  .scent {
    position: absolute; left: 0; right: 0; top: 520px; text-align: center;
    font-family: "Oleo Script", cursive; font-weight: 700; font-size: 42px; line-height: 48px; color: var(--ink);
  }
  .description {
    position: absolute; left: 0; right: 0; top: 594px; text-align: center;
    font-family: "Lato", sans-serif; font-size: 19px; line-height: 29px; color: var(--ink);
  }

  .caption {
    position: absolute; top: 878px; width: 556px; text-align: center;
    font-family: "Crimson Text", serif; font-style: italic; font-weight: 700; font-size: 25px; color: #111;
  }
  .caption--organic { left: 36px; }
  .caption--olive { left: 607px; }
</style>
</head>
<body>
<main class="sheet">

  <section class="label label--organic">
    <svg class="label__art" viewBox="0 0 556 809">
      <rect class="frame" x="49" y="58" width="458" height="686" rx="16" fill="none" stroke="var(--frame)" stroke-width="6"/>
      <rect class="panel" x="70" y="80" width="416" height="650" rx="12" fill="var(--panel)" stroke="var(--panel-edge)" stroke-width="3"/>
      <path class="crest" d="M88,120 Q88,100 108,100 H452 Q472,100 472,120 V300 Q472,320 452,320 H426 V330 Q426,394 279,394 Q132,394 132,330 V320 H108 Q88,320 88,300 Z" fill="var(--crest)" stroke="var(--crest-edge)" stroke-width="4"/>
      <path class="crest__inner" d="M100,124 Q100,112 112,112 H448 Q460,112 460,124 V296 Q460,308 448,308 H414 V328 Q414,382 279,382 Q144,382 144,328 V308 H112 Q100,308 100,296 Z" fill="none" stroke="var(--crest-edge)" stroke-width="1.5" opacity=".6"/>
      <path class="ribbon" role="img" aria-label="Curled parchment ribbon banner" d="M24,168 Q150,150 279,150 Q408,150 538,168 L524,206 L538,250 Q408,232 279,232 Q150,232 24,250 L38,206 Z" fill="var(--ribbon)" stroke="var(--ribbon-shade)" stroke-width="2"/>
      <rect class="crest__soap" role="img" aria-label="Soap bar with olive sprig and leaves" x="182" y="296" width="140" height="76" rx="24" fill="var(--soap-tone)" opacity=".55"/>
      <line x1="219" y1="571" x2="337" y2="571" stroke="var(--ink)" stroke-width="1.5"/>
      <circle cx="278" cy="571" r="2.5" fill="var(--ink)"/>
      <rect class="sprig" role="img" aria-label="Sprig of red berries and leaves" x="290" y="686" width="160" height="36" rx="18" fill="var(--berry)" opacity=".45"/>
    </svg>
    <div class="brand__name">The Brisk Owl</div>
    <div class="brand__line">Organic &amp; Natural Soaps</div>
    <div class="product product__kind" style="left:0;width:556px;top:439px">Organic</div>
    <div class="product product__type" style="left:0;width:556px;top:466px">Bar Soap</div>
    <div class="scent">Dunes</div>
    <p class="description">sandalwood earthy tones with<br>a sandalwood powder exfoliant<br>to smooth your skin</p>
  </section>

  <section class="label label--olive">
    <svg class="label__art" viewBox="0 0 556 809">
      <rect class="frame" x="49" y="58" width="458" height="686" rx="16" fill="none" stroke="var(--frame)" stroke-width="6"/>
      <rect class="panel" x="70" y="80" width="416" height="650" rx="12" fill="var(--panel)" stroke="var(--panel-edge)" stroke-width="3"/>
      <path class="crest" d="M88,120 Q88,100 108,100 H452 Q472,100 472,120 V300 Q472,320 452,320 H426 V330 Q426,394 279,394 Q132,394 132,330 V320 H108 Q88,320 88,300 Z" fill="var(--crest)" stroke="var(--crest-edge)" stroke-width="4"/>
      <path class="crest__inner" d="M100,124 Q100,112 112,112 H448 Q460,112 460,124 V296 Q460,308 448,308 H414 V328 Q414,382 279,382 Q144,382 144,328 V308 H112 Q100,308 100,296 Z" fill="none" stroke="var(--crest-edge)" stroke-width="1.5" opacity=".6"/>
      <path class="ribbon" role="img" aria-label="Curled parchment ribbon banner" d="M24,168 Q150,150 279,150 Q408,150 538,168 L524,206 L538,250 Q408,232 279,232 Q150,232 24,250 L38,206 Z" fill="var(--ribbon)" stroke="var(--ribbon-shade)" stroke-width="2"/>
      <rect class="crest__soap" role="img" aria-label="Soap bar with olive sprig and leaves" x="182" y="296" width="140" height="76" rx="24" fill="var(--soap-tone)" opacity=".55"/>
      <circle class="olive-badge" role="img" aria-label="Green olives with leaves" cx="150" cy="484" r="34" fill="var(--olive)" opacity=".75"/>
      <line x1="219" y1="571" x2="337" y2="571" stroke="var(--ink)" stroke-width="1.5"/>
      <circle cx="278" cy="571" r="2.5" fill="var(--ink)"/>
      <rect class="sprig" role="img" aria-label="Sprig of red berries and leaves" x="160" y="686" width="160" height="36" rx="18" fill="var(--berry)" opacity=".45"/>
    </svg>
    <div class="brand__name">The Brisk Owl</div>
    <div class="brand__line">Organic &amp; Natural Soaps</div>
    <div class="product product__natural" style="left:96px;width:110px;top:423px">Natural</div>
    <div class="product product__kind" style="left:172px;width:220px;top:447px">Olive Oil Based</div>
    <div class="product product__type" style="left:172px;width:220px;top:475px">Bar Soap</div>
    <div class="scent">Dunes</div>
    <p class="description">sandalwood earthy tones with<br>a sandalwood powder exfoliant<br>to smooth your skin</p>
  </section>

  <div class="caption caption--organic">Organic Bar Soap</div>
  <div class="caption caption--olive">Natural Olive Oil Based Bar Soap</div>

</main>
</body>
</html>
```